Velmar Industrial Coatings

We are looking to improve our business cards. Our company installs industrial floor and wall coatings in industrial, chemical and food processing plants.
Our coatings which consist of epoxy, urethane, and vinyl esters provide chemical and abrasion resistant surface with non-skid properties that are easy to clean.

Target Market(s)

food manufacturing, chemical plants, breweries and wineries, warehouses, clean room floors.

Industry/Entity Type

Construction

Contact Information for Business Card

improved current logo.

Colors

Designer to choose colors to be used in the design.

Requirements
Must have
• the information from uploaded file
Nice to have
• "We'll be outstanding on your floors."

```html
<!DOCTYPE html>
<html lang="en">
<head>
<meta charset="utf-8">
<title>Velmar Industrial Coatings – Business Card</title>
<link href="https://fonts.googleapis.com/css2?family=Noto+Serif:ital,wght@0,400;0,700;1,400&family=Open+Sans:wght@300;400&display=swap" rel="stylesheet">
<style>
  :root {
    --backdrop: #e4e4e4;
    --card: #ffffff;
    --ink: #222222;
    --brand-grey: #555555;
    --tagline-grey: #8a8a8a;
    --web-green: #2e8b3e;
  }
  html, body {
    margin: 0;
    padding: 0;
    width: 1200px;
    height: 900px;
    overflow: hidden;
    background: var(--backdrop);
  }
  .canvas {
    position: relative;
    width: 1200px;
    height: 900px;
  }
  .business-card {
    position: absolute;
    left: 100px;
    top: 164px;
    width: 1000px;
    height: 572px;
    background: var(--card);
    box-shadow: 0 2px 10px rgba(0,0,0,0.12);
    font-family: "Noto Serif", Georgia, serif;
    color: var(--ink);
  }
  .brand {
    position: absolute;
    left: 76px;
    top: 74px;
    display: flex;
    align-items: baseline;
    white-space: nowrap;
  }
  .brand-name {
    font-size: 38px;
    font-weight: 700;
    color: var(--brand-grey);
  }
  .brand-tagline {
    margin-left: 14px;
    font-family: "Open Sans", Arial, sans-serif;
    font-weight: 300;
    font-size: 31px;
    letter-spacing: 1px;
    color: var(--tagline-grey);
    text-transform: uppercase;
  }
  .person {
    position: absolute;
    left: 300px;
    top: 165px;
    text-align: center;
  }
  .person-name {
    margin: 0;
    font-size: 34px;
    font-weight: 400;
    letter-spacing: 1px;
    text-transform: uppercase;
  }
  .person-line {
    margin: 4px 0 0;
    font-size: 22px;
    font-style: italic;
    color: #444;
  }
  .phones {
    position: absolute;
    right: 40px;
    top: 230px;
    text-align: right;
    font-size: 22px;
    line-height: 1.45;
  }
  .phones p { margin: 0; }
  .address {
    position: absolute;
    left: 110px;
    top: 420px;
    font-size: 23px;
    line-height: 1.4;
    font-style: normal;
  }
  .address p { margin: 0; }
  .address .address-company { font-weight: 700; }
  .website {
    position: absolute;
    left: 420px;
    top: 440px;
    margin: 16px 0 0;
    font-size: 27px;
    font-style: italic;
    color: var(--web-green);
  }
</style>
</head>
<body>
<main class="canvas">
  <section class="business-card">
    <div class="brand">
      <span class="brand-name">Velmar Inc.</span>
      <span class="brand-tagline">Industrial Coatings</span>
    </div>

    <div class="person">
      <h1 class="person-name">Mark Ellison</h1>
      <p class="person-line">1-800-555-0142</p>
      <p class="person-line">mark@velmarfloors.com</p>
    </div>

    <div class="phones">
      <p>Office (360) 555-0131</p>
      <p>Fax (360) 555-0133</p>
      <p>Cell (360) 555-0176</p>
    </div>

    <address class="address">
      <p class="address-company">Velmar Inc.</p>
      <p>PO Box 42</p>
      <p>Riverton, WA 9851</p>
    </address>

    <p class="website">www.velmarfloors.com</p>
  </section>
</main>
</body>
</html>
```